100% West Australian Static Banner

I require a static banner to go on a couple of pages in our website (under development) that highlights that we are a 100% Western Australian Owned & Operated company. I would prefer the banner to be in our company colours (blue shades & grey). I also would like it to be eye catching and modern in design. I have included a 100% West Australian rubber stamp logo to be used as well as including our logo so you know our colours. The banner needs to be 1139 x 350 pixels in size.

Target Market(s)

B2B

Requirements
Must have
• Our rubber stamp 100% West Australian logo
• Modern Eye Catching design
• Blue shaded background
Nice to have
• Shading background similar our logo blue colours
• 100% logo can be reversed out if required or colour changed
• Larger text saying - 100% West Australian Owned & Operated

```html
<!DOCTYPE html>
<html lang="en">
<head>
<meta charset="utf-8">
<title>100% West Australian Owned &amp; Operated Banner</title>
<link rel="stylesheet" href="https://fonts.googleapis.com/css2?family=Josefin+Sans:wght@600;700&display=swap">
<style>
  :root {
    --page-bg: #ffffff;
    --blue-deep: #0b55a0;
    --blue-mid: #1a5fae;
    --blue-core: #0a76bb;
    --blue-sky: #1a9bd7;
    --blue-bright: #1b9dd8;
    --stamp-tint: #5ea5d6;
    --text-light: #f4f8fb;
  }
  * { margin: 0; padding: 0; box-sizing: border-box; }
  html, body {
    width: 1200px;
    height: 1200px;
    overflow: hidden;
    background: var(--page-bg);
  }
  .canvas {
    position: relative;
    width: 1200px;
    height: 1200px;
  }
  .banner {
    position: absolute;
    left: 92px;
    top: 394px;
    width: 1003px;
    height: 308px;
    background: linear-gradient(90deg,
      var(--blue-deep) 0%,
      var(--blue-mid) 17%,
      var(--blue-core) 32%,
      var(--blue-sky) 58%,
      var(--blue-bright) 100%);
    overflow: hidden;
  }
  .stamp-badge {
    position: absolute;
    left: 13px;
    top: 28px;
    width: 238px;
    height: 238px;
  }
  .headline {
    position: absolute;
    left: 262px;
    right: 0;
    top: 95px;
    text-align: center;
    font-family: "Josefin Sans", sans-serif;
    font-weight: 700;
    font-size: 56px;
    line-height: 64px;
    letter-spacing: 1px;
    color: var(--text-light);
    text-transform: uppercase;
  }
  .headline span { display: block; }
</style>
</head>
<body>
  <div class="canvas">
    <section class="banner" aria-label="100% West Australian owned and operated">
      <svg class="stamp-badge" viewBox="0 0 238 238" role="img" aria-label="Ownership stamp badge">
        <circle cx="119" cy="119" r="116" fill="var(--stamp-tint)" opacity="0.85"/>
      </svg>
      <h1 class="headline">
        <span>100% West Australian</span>
        <span>Owned &amp; Operated</span>
      </h1>
    </section>
  </div>
</body>
</html>
```